Ridgeway Fluidworks needs a website describing the repair business we are in.

Ridgeway Fluidworks is a full hydraulic repair facility. We have 2 shops. We repair and service all hydraulic cylinders, pneumatic cylinders, hydraulic pumps, motors, valves and gearboxes. Our services range from large industrial plants to the individual that owns one piece of equipment. We also offer removal and install of cylinders. Along with free pick up and delivery, within a certain distance which is usually 100 miles from one of our shops.

With over 30 years experience in the hydraulic business, we can repair or replace any job. There is not a job too big or too small, we service them all.

We have customers that send whole pieces of equipment to us to do complete overhauls on all the hydraulics. Ranging from a country club green roller to a 10 ton boom truck.

Target Market(s)

Industrial plants, road builders, dirt work companies, general contractors, owners of industrial equipment (bulldozers, excavators, loaders, scrapers, motor graders, etc.

Industry/Entity Type

Hydraulic

Number of Pages Required

5+ page

Font styles to use
Sans Serif

Colors
ec1f27
ffffff
aaaaaa

Requirements
Must have
• Information about what we offer and pictures of jobs completed.
Nice to have
• Nice stock photos of jobsites and industrial plants.
Should not have
• Any sort of comical characters.

```html
<!DOCTYPE html>
<html lang="en">
<head>
<meta charset="utf-8">
<title>Ridgeway Fluidworks — Full Hydraulic Repair Facility</title>
<link href="https://fonts.googleapis.com/css2?family=Lato:ital,wght@0,400;0,700;0,900;1,400&display=swap" rel="stylesheet">
<style>
:root{
  --red:#ec1f27;
  --red-dark:#b5121a;
  --white:#ffffff;
  --grey:#aaaaaa;
  --btn-grey:#8c8c8c;
  --ink:#1e1e1e;
  --body:#3a3a3a;
  --panel:#f0f0f0;
}
*{margin:0;padding:0;box-sizing:border-box}
html,body{width:1200px;height:3158px;overflow:hidden}
body{font-family:'Lato',sans-serif;color:var(--body);background:var(--white);position:relative}
.section{position:absolute;left:0;width:1200px}
.wrap{position:absolute;left:76px;width:1050px}

/* header */
.site-header{top:0;height:139px;background:var(--white)}
.brand{position:absolute;left:76px;top:18px;display:flex;align-items:center;gap:12px}
.brand-dot{width:56px;height:56px;border-radius:50%;background:var(--red);flex:none}
.brand-name{font-weight:900;font-size:22px;line-height:24px;color:var(--red);text-transform:uppercase;width:140px}
.header-phone{position:absolute;left:712px;top:32px;display:flex;align-items:center;gap:10px;font-size:23px;color:var(--ink)}
.btn-request{position:absolute;left:928px;top:27px;width:196px;height:36px;background:var(--red);color:var(--white);font-size:13px;font-weight:700;text-transform:uppercase;display:flex;align-items:center;justify-content:center;border-radius:2px}
.main-nav{position:absolute;right:74px;top:93px;display:flex;gap:30px;font-size:14.5px;color:var(--ink);text-transform:uppercase}
.main-nav .active{color:var(--red)}

/* hero */
.hero{top:139px;height:522px;background:linear-gradient(180deg,#8f9a8c 0%,#b9b6ae 18%,#a19c93 45%,#4a4742 70%,#2c2a27 100%)}
.hero-title{position:absolute;left:0;right:0;top:190px;text-align:center;font-weight:700;font-size:51px;line-height:72px;color:var(--white)}
.hero-title span{background:rgba(200,22,30,.72);padding:0 12px}
.hero-dots{position:absolute;left:570px;top:482px;display:flex;gap:8px}
.hero-dots i{width:9px;height:9px;border-radius:50%;background:var(--white)}
.hero-dots i.on{background:var(--red)}

/* headings */
.heading{font-weight:700;font-size:30px;color:var(--ink);text-transform:uppercase;letter-spacing:.3px}
.heading::after{content:"";display:block;width:106px;height:4px;background:var(--red);margin-top:14px}
.heading.center{text-align:center}
.heading.center::after{margin-left:auto;margin-right:auto}
.btn-grey{display:flex;align-items:center;justify-content:center;background:var(--btn-grey);color:var(--white);font-size:14px;font-weight:700;text-transform:uppercase;border-radius:2px}
.photo{background:linear-gradient(135deg,#6f6a62,#b8ad8f 50%,#3f3c38)}

/* welcome */
.welcome{top:661px;height:379px}
.welcome .heading{position:absolute;left:76px;top:40px}
.welcome-text{position:absolute;left:76px;top:108px;width:600px;font-size:14.5px;line-height:28px}
.welcome .btn-grey{position:absolute;left:76px;top:282px;width:150px;height:45px}
.welcome-photo{position:absolute;left:705px;top:46px;width:421px;height:280px;background:linear-gradient(135deg,#d8a718 0%,#7d8a94 40%,#c9d0d6 60%,#c4961a 100%)}

/* what we do */
.what{top:1040px;height:543px;background:var(--panel)}
.what .heading{position:absolute;top:42px;left:0;right:0}
.cards{position:absolute;left:76px;top:137px;width:1050px;display:flex;gap:26px}
.card{width:243px;text-align:center}
.card-photo{height:136px}
.card-title{margin-top:24px;font-size:16px;font-weight:700;color:var(--red);text-transform:uppercase}
.card-text{margin-top:6px;font-size:14.5px;line-height:25px;color:var(--ink)}
.what .btn-grey{position:absolute;left:509px;top:442px;width:181px;height:46px}

/* service offers */
.offers{top:1583px;height:444px}
.offers .heading{position:absolute;top:42px;left:0;right:0}
.offer-list{position:absolute;left:76px;top:138px;width:1050px;display:flex;justify-content:space-between;padding:0 2px}
.offer{width:260px;text-align:center}
.offer-icon{width:126px;height:126px;border-radius:50%;margin:0 auto;background:linear-gradient(160deg,var(--red) 50%,var(--grey) 50%);display:flex;align-items:center;justify-content:center}
.offer-title{margin-top:26px;font-size:16px;font-weight:700;color:var(--red);text-transform:uppercase}
.offer-text{margin-top:6px;font-size:14.5px;line-height:25px;color:var(--ink)}

/* gallery */
.gallery{top:2027px;height:556px;background:var(--panel)}
.gallery .heading{position:absolute;top:42px;left:0;right:0}
.gallery-item{position:absolute}

/* blog & testimonials */
.news{top:2583px;height:324px}
.news .heading{position:absolute;top:38px}
.arrows{position:absolute;top:44px;display:flex;gap:14px}
.blog-photo{position:absolute;left:76px;top:120px;width:240px;height:160px;background:linear-gradient(135deg,#5b5650,#b8a77f 55%,#3a3733)}
.blog-title{position:absolute;left:343px;top:120px;font-size:18px;font-weight:700;color:var(--red)}
.blog-text{position:absolute;left:343px;top:152px;width:400px;font-size:14.5px;line-height:26px;color:var(--ink)}
.news .btn-grey{position:absolute;left:343px;top:236px;width:152px;height:44px}
.quote{position:absolute;left:794px;top:112px;width:334px;font-size:13.5px;line-height:26px;font-style:italic;color:var(--ink)}
.quote-name{position:absolute;left:794px;top:225px;font-size:15px;font-weight:700;color:var(--red)}
.quote-role{position:absolute;left:794px;top:248px;font-size:13.5px;font-style:italic;color:var(--ink)}

/* footer */
.site-footer{top:2907px;height:251px;background:linear-gradient(180deg,var(--red) 0%,var(--red-dark) 100%);color:var(--white)}
.footer-brand{position:absolute;left:76px;top:40px;display:flex;align-items:center;gap:10px}
.footer-brand .brand-dot{background:var(--white);width:50px;height:50px}
.footer-brand .brand-name{color:var(--white);font-size:20px;line-height:22px}
.copyright{position:absolute;left:76px;top:166px;font-size:12.5px;line-height:24px}
.foot-title{position:absolute;top:44px;font-size:15px;font-weight:700;text-transform:uppercase}
.sitemap{position:absolute;left:343px;top:80px;display:grid;grid-template-columns:100px 100px;row-gap:6px;font-size:13px;line-height:22px}
.contact{position:absolute;left:613px;top:80px;font-size:13px;line-height:24px}
.contact li{list-style:none;display:flex;gap:12px;align-items:center}
.signup{position:absolute;left:884px;top:80px;width:242px;height:36px;display:flex}
.signup-field{flex:1;background:var(--white);color:var(--ink);font-size:13px;display:flex;align-items:center;gap:10px;padding-left:12px}
.signup-go{width:40px;background:var(--btn-grey);color:var(--white);font-weight:700;font-size:14px;display:flex;align-items:center;justify-content:center}
.social{position:absolute;left:884px;top:165px;display:flex;gap:17px}
.social i{width:22px;height:22px;border-radius:50%;background:var(--white)}
</style>
</head>
<body>

<header class="section site-header">
  <div class="brand"><span class="brand-dot"></span><span class="brand-name">Ridgeway Fluidworks</span></div>
  <div class="header-phone">
    <svg width="18" height="18" viewBox="0 0 24 24"><path fill="#ec1f27" d="M6.6 10.8a15.1 15.1 0 0 0 6.6 6.6l2.2-2.2c.3-.3.7-.4 1-.2 1.1.4 2.3.6 3.6.6.6 0 1 .4 1 1V20c0 .6-.4 1-1 1A17 17 0 0 1 3 4c0-.6.4-1 1-1h3.5c.6 0 1 .4 1 1 0 1.3.2 2.5.6 3.6.1.3 0 .7-.2 1z"/></svg>
    1-800-555-0142
  </div>
  <div class="btn-request">Request a Service</div>
  <nav class="main-nav">
    <span class="active">Home</span><span>About Us</span><span>Services</span><span>Blog</span><span>Testimonials</span><span>Careers</span><span>Contact Us</span>
  </nav>
</header>

<section class="section hero" role="img" aria-label="Photo of a yellow hydraulic cylinder strapped onto a flatbed trailer parked on a concrete lot">
  <h1 class="hero-title"><span>Ridgeway Fluidworks is a</span><br><span>Full Hydraulic Repair Facility.</span></h1>
  <div class="hero-dots"><i class="on"></i><i></i><i></i><i></i></div>
</section>

<section class="section welcome">
  <h2 class="heading">Welcome to our website</h2>
  <p class="welcome-text">Aliquam molestie, mi et imperdiet euismod, dui purus auctor tellus, et interdum lacus lectus et ante. Sed accumsan sollicitudin sapien, sit amet adipiscing turpis gravida ac. In congue, neque ac lobortis volutpat, libero mauris varius mi, vitae suscipit ipsum ligula vitae risus. Duis aliquam nibh a dui iaculis viverra id a velit. Vivamus egestas risus in magna varius commodo. Sed semper viverra egestas.</p>
  <div class="btn-grey">Read More</div>
  <div class="welcome-photo" role="img" aria-label="Close-up photo of a steel hydraulic cylinder with yellow machinery"></div>
</section>

<section class="section what">
  <h2 class="heading center">What we do</h2>
  <div class="cards">
    <div class="card"><div class="card-photo photo" role="img" aria-label="Photo of hydraulic cylinders on a workbench"></div><h3 class="card-title">Hydraulic Cylinders</h3><p class="card-text">Aliquam molestie, mi et imperdiet euismod, dui purus auctor tellus, et interdum lacus lectus et ante.</p></div>
    <div class="card"><div class="card-photo" style="background:linear-gradient(135deg,#e0b21c,#8a7a3a 60%,#3b3a36)" role="img" aria-label="Photo of yellow pneumatic cylinder assembly"></div><h3 class="card-title">Pneumatic Cylinders</h3><p class="card-text">Aliquam molestie, mi et imperdiet euismod, dui purus auctor tellus, et interdum lacus lectus et ante.</p></div>
    <div class="card"><div class="card-photo" style="background:linear-gradient(135deg,#5f6a6e,#8d7c62 50%,#c9c4b8)" role="img" aria-label="Photo of a hydraulic pump on display"></div><h3 class="card-title">Hydraulic Pumps</h3><p class="card-text">Aliquam molestie, mi et imperdiet euismod, dui purus auctor tellus, et interdum lacus lectus et ante.</p></div>
    <div class="card"><div class="card-photo" style="background:linear-gradient(135deg,#4b4f55,#b7bcc0 50%,#6e7378)" role="img" aria-label="Photo of steel valves and gearbox gears"></div><h3 class="card-title">Valves &amp; Gearboxes</h3><p class="card-text">Aliquam molestie, mi et imperdiet euismod, dui purus auctor tellus, et interdum lacus lectus et ante.</p></div>
  </div>
  <div class="btn-grey">View All Services</div>
</section>

<section class="section offers">
  <h2 class="heading center">Our service offers</h2>
  <div class="offer-list">
    <div class="offer">
      <div class="offer-icon"><svg width="60" height="52" viewBox="0 0 60 52" fill="#fff"><rect x="8" y="4" width="7" height="20"/><path d="M4 48V26l14 8v-8l14 8v-8l14 8V20h8v28z"/><rect x="14" y="38" width="6" height="5" fill="#aaaaaa"/><rect x="26" y="38" width="6" height="5" fill="#aaaaaa"/><rect x="38" y="38" width="6" height="5" fill="#aaaaaa"/></svg></div>
      <h3 class="offer-title">Large Industrial Plants</h3><p class="offer-text">Aliquam molestie, mi et imperdiet euismod, dui purus auctor tellus</p>
    </div>
    <div class="offer">
      <div class="offer-icon"><svg width="60" height="60" viewBox="0 0 60 60"><g transform="rotate(-45 30 30)"><rect x="4" y="23" width="30" height="14" rx="2" fill="#fff"/><rect x="34" y="27" width="20" height="6" fill="#fff"/><circle cx="55" cy="30" r="4" fill="none" stroke="#fff" stroke-width="2.5"/></g></svg></div>
      <h3 class="offer-title">Individual</h3><p class="offer-text">Aliquam molestie, mi et imperdiet euismod, dui purus auctor tellus</p>
    </div>
    <div class="offer">
      <div class="offer-icon"><svg width="62" height="62" viewBox="0 0 62 62"><g fill="#fff"><circle cx="31" cy="31" r="19"/><g><rect x="27" y="4" width="8" height="10"/><rect x="27" y="48" width="8" height="10"/><rect x="4" y="27" width="10" height="8"/><rect x="48" y="27" width="10" height="8"/><rect x="27" y="4" width="8" height="10" transform="rotate(45 31 31)"/><rect x="27" y="48" width="8" height="10" transform="rotate(45 31 31)"/><rect x="4" y="27" width="10" height="8" transform="rotate(45 31 31)"/><rect x="48" y="27" width="10" height="8" transform="rotate(45 31 31)"/></g></g><circle cx="31" cy="31" r="11" fill="#aaaaaa"/><path d="M25 25l12 12M37 25L25 37" stroke="#fff" stroke-width="3"/></svg></div>
      <h3 class="offer-title">Removal &amp; Install</h3><p class="offer-text">Aliquam molestie, mi et imperdiet euismod, dui purus auctor tellus</p>
    </div>
    <div class="offer">
      <div class="offer-icon"><svg width="66" height="46" viewBox="0 0 66 46" fill="#fff"><rect x="2" y="2" width="38" height="30"/><path d="M42 12h12l10 12v12H42z"/><circle cx="14" cy="38" r="6"/><circle cx="52" cy="38" r="6"/></svg></div>
      <h3 class="offer-title">Free Pick Up &amp; Delivery</h3><p class="offer-text">Aliquam molestie, mi et imperdiet euismod, dui purus auctor tellus</p>
    </div>
  </div>
</section>

<section class="section gallery">
  <h2 class="heading center">Gallery</h2>
  <div class="gallery-item" style="left:76px;top:135px;width:252px;height:177px;background:linear-gradient(135deg,#4a443c,#b9b7b2 55%,#7b6a55)" role="img" aria-label="Photo of two grey hydraulic cylinders on a crate"></div>
  <div class="gallery-item" style="left:343px;top:135px;width:251px;height:177px;background:linear-gradient(135deg,#6d6862,#a7a29a 50%,#c9bca4)" role="img" aria-label="Photo of cylinder rods laid on a wooden pallet"></div>
  <div class="gallery-item" style="left:608px;top:135px;width:518px;height:177px;background:linear-gradient(135deg,#6e5a3e,#d8b42a 45%,#a8916a)" role="img" aria-label="Photo of yellow hydraulic cylinders on wooden pallets"></div>
  <div class="gallery-item" style="left:76px;top:326px;width:518px;height:177px;background:linear-gradient(135deg,#5a4a3a,#e0602a 50%,#3e3b36)" role="img" aria-label="Photo of a large orange hydraulic cylinder strapped to a pallet"></div>
  <div class="gallery-item" style="left:608px;top:326px;width:253px;height:177px;background:linear-gradient(135deg,#5b3a30,#a9463a 50%,#8b7a66)" role="img" aria-label="Photo of red cylinders on a shop pallet"></div>
  <div class="gallery-item" style="left:874px;top:326px;width:252px;height:177px;background:linear-gradient(135deg,#3e3e44,#2a2a33 50%,#9a9a9a)" role="img" aria-label="Photo of black cylinders on a shop floor"></div>
</section>

<section class="section news">
  <h2 class="heading" style="left:76px">Blog posts</h2>
  <div class="arrows" style="left:694px"><svg width="12" height="20" viewBox="0 0 12 20"><path d="M10 2L2 10l8 8" fill="none" stroke="#1e1e1e" stroke-width="3"/></svg><svg width="12" height="20" viewBox="0 0 12 20"><path d="M2 2l8 8-8 8" fill="none" stroke="#1e1e1e" stroke-width="3"/></svg></div>
  <div class="blog-photo" role="img" aria-label="Photo of a hydraulic component on a wooden pallet"></div>
  <h3 class="blog-title">Aliquam molestie mi et imperdiet euismod</h3>
  <p class="blog-text">Dui purus auctor tellus, et interdum lacus lectus et ante sed accumsan sollicitudin sapien, sit amet adipiscing turpis gravida ac neque ac lobortis volutpat..</p>
  <div class="btn-grey">Read More</div>

  <h2 class="heading" style="left:794px">Testimonials</h2>
  <div class="arrows" style="left:1086px"><svg width="12" height="20" viewBox="0 0 12 20"><path d="M10 2L2 10l8 8" fill="none" stroke="#1e1e1e" stroke-width="3"/></svg><svg width="12" height="20" viewBox="0 0 12 20"><path d="M2 2l8 8-8 8" fill="none" stroke="#1e1e1e" stroke-width="3"/></svg></div>
  <p class="quote">“ Dui purus auctor tellus, et interdum lacus lectus et ante sed accumsan sollicitudin sapien, sit amet adipiscing turpis gravida ac neque ac lobortis volutpat....”</p>
  <div class="quote-name">Name Heading</div>
  <div class="quote-role">Company</div>
</section>

<footer class="section site-footer">
  <div class="footer-brand"><span class="brand-dot"></span><span class="brand-name">Ridgeway Fluidworks</span></div>
  <p class="copyright">Copyright © 2018. Company Name<br>All Right Reserved</p>

  <h4 class="foot-title" style="left:343px">Site Map</h4>
  <div class="sitemap"><span>Home</span><span>Testimonials</span><span>About Us</span><span>Careers</span><span>Services</span><span>Contact Us</span><span>Blog</span></div>

  <h4 class="foot-title" style="left:613px">Contact Address</h4>
  <ul class="contact">
    <li>412 Copperline Road,</li>
    <li>Ashford, R12 7KT</li>
    <li><svg width="12" height="12" viewBox="0 0 24 24"><path fill="#fff" d="M6.6 10.8a15.1 15.1 0 0 0 6.6 6.6l2.2-2.2c.3-.3.7-.4 1-.2 1.1.4 2.3.6 3.6.6.6 0 1 .4 1 1V20c0 .6-.4 1-1 1A17 17 0 0 1 3 4c0-.6.4-1 1-1h3.5c.6 0 1 .4 1 1 0 1.3.2 2.5.6 3.6.1.3 0 .7-.2 1z"/></svg>1-800-555-0142</li>
    <li><svg width="12" height="10" viewBox="0 0 24 18"><path fill="#fff" d="M0 0h24v18H0z"/><path d="M1 1l11 9 11-9" fill="none" stroke="#c4151d" stroke-width="2"/></svg>info@ridgewayfluidworks.com</li>
  </ul>

  <h4 class="foot-title" style="left:884px">Email Sign Up</h4>
  <div class="signup">
    <div class="signup-field"><svg width="13" height="10" viewBox="0 0 24 18"><path fill="#1e1e1e" d="M0 0h24v18H0z"/><path d="M1 1l11 9 11-9" fill="none" stroke="#fff" stroke-width="2"/></svg>Enter Email</div>
    <div class="signup-go">GO</div>
  </div>
  <h4 class="foot-title" style="left:884px;top:133px">Follow Us</h4>
  <div class="social" aria-label="Social links"><i></i><i></i><i></i><i></i><i></i></div>
</footer>

</body>
</html>
```